Company Values Graphic

We are looking for a design of our company values that can be used in a variety of places including our website, mousepads, office posters, business cards, etc.

Notes:
- We'd rather have icons/art than photographs on the poster.... so more like an infographic
- The core value group headings are not required, but can be included if you think grouping the values works for your design
- We have a logo for our software product but that logo is not required
- We don't need/want clever images to accompany each value, but some images are fine
- BrisKel logo attached
- BrisKel colors are attached
- BrisKel logo is Nunito Sans ExtraBold 800
- BrisKel website uses Roboto

Our Values - Who we will work with (and who we will not)
The right set of values are essential to building and maintaining a culture that we all wake up eager to be a part of each day. They are foundational to all hiring and firing decisions. They attract the right people and repel the wrong ones.

BE HELPFUL
Make every person and place better because you are there.
Deliver wow with every interaction.

BE HUMBLE
Listen with every muscle.
Passionately help others first.
Seek first to understand.

BE HONEST
Earn trust every day.
Be open and direct.
Treat everyone with fairness and respect.

BE HUMAN
Celebrate passion and action.
Create an environment where people are authentic.
Hire great people and expect a lot from them

BE COURAGEOUS
Dare mighty things.
Make and honor commitments.
All great things start with a small act of courage applied at the right moment.

```html
<!DOCTYPE html>
<html lang="en">
<head>
<meta charset="utf-8">
<title>BrisKel – Our Values</title>
<link rel="stylesheet" href="https://fonts.googleapis.com/css2?family=Montserrat:wght@400;500;700;800&family=Roboto:wght@400;500&display=swap">
<style>
  :root {
    --page-bg: #e9e9e9;
    --card-bg: #ffffff;
    --stripe-grey: #f2f2f2;
    --ring-light: #f7f7f7;
    --ring-dark: #d9d9d9;
    --red-1: #ec2024;
    --red-2: #e83227;
    --orange-3: #ef5a24;
    --orange-4: #f37a20;
    --orange-5: #f7a01e;
    --ink: #111111;
    --white: #ffffff;
  }
  html, body {
    margin: 0;
    padding: 0;
    width: 800px;
    height: 1200px;
    overflow: hidden;
    background: var(--page-bg);
  }
  .values-card {
    position: absolute;
    left: 20px;
    top: 306px;
    width: 760px;
    height: 588px;
    background: var(--card-bg);
    box-shadow: 0 6px 14px rgba(0,0,0,0.22);
    overflow: hidden;
  }
  .card-art {
    position: absolute;
    inset: 0;
  }
  .brand {
    position: absolute;
    left: 31px;
    top: 168px;
    display: flex;
    align-items: center;
    gap: 9px;
  }
  .brand-dot {
    width: 24px;
    height: 24px;
    border-radius: 50%;
    background: var(--orange-3);
  }
  .brand-name {
    font-family: "Montserrat", sans-serif;
    font-weight: 700;
    font-size: 25px;
    color: var(--ink);
    letter-spacing: -0.3px;
  }
  .intro-title {
    position: absolute;
    left: 33px;
    top: 218px;
    margin: 0;
    font-family: "Montserrat", sans-serif;
    font-size: 21.5px;
    line-height: 25px;
    font-weight: 800;
    color: var(--red-1);
  }
  .intro-title .title-aside {
    display: block;
    font-weight: 500;
    color: var(--orange-3);
  }
  .intro-text {
    position: absolute;
    left: 33px;
    top: 336px;
    width: 196px;
    margin: 0;
    font-family: "Roboto", sans-serif;
    font-size: 11.2px;
    line-height: 14px;
    color: var(--ink);
  }
  .value {
    position: absolute;
    display: flex;
    align-items: center;
    color: var(--white);
  }
  .value-number {
    font-family: "Montserrat", sans-serif;
    font-weight: 700;
    font-size: 36px;
    line-height: 1;
    width: 60px;
    flex: none;
  }
  .value-title {
    margin: 0 0 2px;
    font-family: "Montserrat", sans-serif;
    font-weight: 800;
    font-size: 22px;
    line-height: 1;
    letter-spacing: 0.3px;
  }
  .value-text {
    margin: 0;
    font-family: "Roboto", sans-serif;
    font-size: 12.6px;
    line-height: 16px;
  }
  .value--helpful { left: 267px; top: 30px; }
  .value--humble { left: 333px; top: 147px; }
  .value--honest { left: 401px; top: 264px; }
  .value--human { left: 333px; top: 374px; }
  .value--courageous { left: 267px; top: 491px; }
  .value--human .value-number { width: 67px; }
  .value--humble .value-number { width: 65px; }
</style>
</head>
<body>
<main class="values-card">
  <svg class="card-art" width="760" height="588" viewBox="0 0 760 588" aria-hidden="false">
    <defs>
      <clipPath id="band-area">
        <polygon points="167,0 760,0 760,588 167,588 300,294"/>
      </clipPath>
      <linearGradient id="ring-shade" x1="0" y1="0" x2="1" y2="1">
        <stop offset="0" stop-color="var(--ring-light)"/>
        <stop offset="1" stop-color="var(--ring-dark)"/>
      </linearGradient>
      <filter id="soft-shadow" x="-20%" y="-20%" width="140%" height="140%">
        <feDropShadow dx="0" dy="3" stdDeviation="3" flood-opacity="0.25"/>
      </filter>
    </defs>

    <polygon class="diagonal-stripe" points="108,0 167,0 300,294 167,588 108,588 241,294" fill="var(--stripe-grey)"/>

    <g class="value-bands" clip-path="url(#band-area)">
      <rect x="0" y="0" width="760" height="118" fill="var(--red-1)"/>
      <rect x="0" y="117" width="760" height="119" fill="var(--red-2)"/>
      <rect x="0" y="235" width="760" height="119" fill="var(--orange-3)"/>
      <rect x="0" y="353" width="760" height="118" fill="var(--orange-4)"/>
      <rect x="0" y="470" width="760" height="118" fill="var(--orange-5)"/>
      <g stroke="rgba(0,0,0,0.12)" stroke-width="1">
        <line x1="0" y1="117.5" x2="760" y2="117.5"/>
        <line x1="0" y1="235.5" x2="760" y2="235.5"/>
        <line x1="0" y1="353.5" x2="760" y2="353.5"/>
        <line x1="0" y1="470.5" x2="760" y2="470.5"/>
      </g>
    </g>

    <g class="value-badges">
      <g class="badge" transform="translate(200,59)">
        <polygon points="-50,0 -25,-43 25,-43 50,0 25,43 -25,43" fill="url(#ring-shade)" filter="url(#soft-shadow)"/>
        <polygon role="img" aria-label="Line icon of two people talking with a speech bubble" points="-34,0 -17,-29 17,-29 34,0 17,29 -17,29" fill="var(--red-1)"/>
      </g>
      <g class="badge" transform="translate(267,176)">
        <polygon points="-50,0 -25,-43 25,-43 50,0 25,43 -25,43" fill="url(#ring-shade)" filter="url(#soft-shadow)"/>
        <polygon role="img" aria-label="Line icon of a calm seated person" points="-34,0 -17,-29 17,-29 34,0 17,29 -17,29" fill="var(--red-2)"/>
      </g>
      <g class="badge" transform="translate(333,294)">
        <polygon points="-50,0 -25,-43 25,-43 50,0 25,43 -25,43" fill="url(#ring-shade)" filter="url(#soft-shadow)"/>
        <polygon role="img" aria-label="Line icon of a person giving a thumbs up" points="-34,0 -17,-29 17,-29 34,0 17,29 -17,29" fill="var(--orange-3)"/>
      </g>
      <g class="badge" transform="translate(267,411)">
        <polygon points="-50,0 -25,-43 25,-43 50,0 25,43 -25,43" fill="url(#ring-shade)" filter="url(#soft-shadow)"/>
        <polygon role="img" aria-label="Line icon of a person with raised arms" points="-34,0 -17,-29 17,-29 34,0 17,29 -17,29" fill="var(--orange-4)"/>
      </g>
      <g class="badge" transform="translate(200,529)">
        <polygon points="-50,0 -25,-43 25,-43 50,0 25,43 -25,43" fill="url(#ring-shade)" filter="url(#soft-shadow)"/>
        <polygon role="img" aria-label="Line icon of a raised fist" points="-34,0 -17,-29 17,-29 34,0 17,29 -17,29" fill="var(--orange-5)"/>
      </g>
    </g>
  </svg>

  <div class="brand">
    <span class="brand-dot"></span>
    <span class="brand-name">BrisKel</span>
  </div>

  <h1 class="intro-title">WHO WE WILL<br>WORK WITH<span class="title-aside">(AND WHO WE<br>WILL NOT)</span></h1>

  <p class="intro-text">The right set of values are essential to building and maintaining a culture that we all wake up eager to be a part of each day. They are foundational to all hiring and firing decisions. They attract the right people and repel the wrong ones.</p>

  <section class="value value--helpful">
    <span class="value-number">01</span>
    <div>
      <h2 class="value-title">BE HELPFUL</h2>
      <p class="value-text">Make every person and place better because you are there.<br>Deliver wow with every interaction.</p>
    </div>
  </section>

  <section class="value value--humble">
    <span class="value-number">02</span>
    <div>
      <h2 class="value-title">BE HUMBLE</h2>
      <p class="value-text">Listen with every muscle. Passionately help others first.<br>Seek first to understand.</p>
    </div>
  </section>

  <section class="value value--honest">
    <span class="value-number">03</span>
    <div>
      <h2 class="value-title">BE HONEST</h2>
      <p class="value-text">Earn trust every day. Be open and direct.<br>Treat everyone with fairness and respect.</p>
    </div>
  </section>

  <section class="value value--human">
    <span class="value-number">04</span>
    <div>
      <h2 class="value-title">BE HUMAN</h2>
      <p class="value-text">Celebrate passion and action.<br>Create an environment where people are authentic.<br>Hire great people and expect a lot from them</p>
    </div>
  </section>

  <section class="value value--courageous">
    <span class="value-number">05</span>
    <div>
      <h2 class="value-title">BE COURAGEOUS</h2>
      <p class="value-text">Dare mighty things. Make and honor commitments.<br>All great things start with a small act of courage applied<br>at the right moment.</p>
    </div>
  </section>
</main>
</body>
</html>
```